MUG MISSION // ROAST REMEDIES // QUIETLY BREWED

website that looks kind of: www.kettlow.com OR PIXELHERDS
I sell coffee to sports teams at a very low price and they make the profit for whatever they are looking to raise money for. This is a tool for them to raise money.
I need help creating not just the website but a catchy name for this project.
Now students don't need to wash cars to raise funds, they have my coffee they can sell to turn it into their own profits.

Target Market(s)

sports teams, schools, churches, fundraisers.

Industry/Entity Type

coffee // fundraiser

Coding

Coded - Design and coding required

Number of Pages Required

1 page

Font styles to use
Serif

Colors
0054AA
0677BA
7BADD7
CADEEF
E8F1F8

Requirements
Must have
• Video of how it works (steps) // Get started button // personalize your coffee bag
Nice to have
• Vandu.com for example as a name for the website

```html
<!DOCTYPE html>
<html lang="en">
<head>
<meta charset="utf-8">
<title>Vandu – Coffee Fundraising</title>
<link href="https://fonts.googleapis.com/css2?family=Bebas+Neue&family=Archivo:wght@400;500;600&family=Poppins:wght@300;400;500;600&display=swap" rel="stylesheet">
<style>
:root{
  --blue-deep:#0054AA;
  --blue-mid:#0677BA;
  --blue-soft:#7BADD7;
  --blue-pale:#CADEEF;
  --blue-mist:#E8F1F8;
  --ink:#111418;
  --grey:#6b6f76;
  --line:#e6e9ee;
  --white:#ffffff;
}
*{margin:0;padding:0;box-sizing:border-box}
html,body{width:1200px;height:4386px;overflow:hidden}
body{position:relative;background:var(--white);font-family:"Poppins",sans-serif;color:var(--ink)}
.abs{position:absolute}
.photo{position:absolute}
.h-section{font-family:"Archivo",sans-serif;font-weight:500;font-size:33px;line-height:38px;text-align:center;letter-spacing:.3px;color:var(--ink)}
.btn{position:absolute;display:flex;align-items:center;justify-content:center;background:var(--blue-mid);color:var(--white);font-family:"Poppins",sans-serif;font-weight:500;font-size:14px;border-radius:6px;letter-spacing:.3px}
.dots{position:absolute;background:var(--blue-pale);opacity:.55}

/* header */
.hero-bg{left:0;top:0;width:1200px;height:740px;background:linear-gradient(180deg,#eef4fa 0%,#ffffff 60%)}
.logo{left:60px;top:18px;font-size:37px;font-weight:500;color:var(--blue-deep);letter-spacing:.5px}
.nav{left:484px;top:33px;display:flex;gap:20px;font-size:11px;color:#333;white-space:nowrap}
.nav .active{color:var(--blue-deep);border-bottom:2px solid var(--blue-deep);padding-bottom:3px}
.btn-login{left:926px;top:23px;width:75px;height:37px;border:1.5px solid var(--blue-deep);border-radius:6px;color:var(--blue-deep);font-size:13px;display:flex;align-items:center;justify-content:center}
.btn-start-top{left:1009px;top:23px;width:131px;height:37px;background:var(--blue-deep);font-size:13px}
.hero-title{left:0;width:1200px;font-family:"Bebas Neue",sans-serif;font-size:46px;text-align:center;color:var(--ink);letter-spacing:.5px}
.hero-ghost{left:0;top:235px;width:1200px;text-align:center;font-family:"Archivo",sans-serif;font-weight:600;font-size:150px;letter-spacing:30px;color:#eef3f9}

/* welcome */
.welcome-bg{left:0;top:732px;width:1200px;height:556px;background:linear-gradient(180deg,#ffffff 0%,var(--blue-mist) 100%)}
.welcome-tag{left:0;width:1232px;top:846px;text-align:center;font-size:14px;color:var(--blue-deep)}
.welcome-bar{left:134px;top:946px;width:11px;height:235px;background:var(--blue-deep)}
.welcome-h{left:575px;top:894px;font-family:"Archivo",sans-serif;font-weight:500;font-size:31px;line-height:41px;letter-spacing:.5px}
.welcome-p{left:703px;top:992px;width:366px;font-size:11px;line-height:19.5px;color:var(--grey)}
.welcome-p p+p{margin-top:10px}

/* flavors */
.flavor-sub{left:0;width:1200px;top:1449px;text-align:center;font-size:14px;color:var(--blue-deep)}
.flavor-row{position:absolute;left:133px;width:936px;height:150px}
.flavor-circle{position:absolute;left:0;width:122px;height:122px;border-radius:50%;background:var(--blue-mist)}
.flavor-bag{position:absolute;left:31px;top:14px;width:60px;height:92px;border-radius:4px;background:linear-gradient(180deg,#c8a47a,#e9d7bd);display:flex;align-items:center;justify-content:center;font-size:12px;font-weight:500;color:#2b2b2b}
.flavor-name{position:absolute;left:165px;font-family:"Archivo",sans-serif;font-weight:500;font-size:18px}
.flavor-desc{position:absolute;left:165px;font-size:12px;color:var(--grey)}
.flavor-price{position:absolute;left:674px;font-family:"Archivo",sans-serif;font-weight:600;font-size:24px;color:var(--blue-deep)}
.flavor-price small{font-size:9px;font-weight:400;color:#444;vertical-align:super;margin-left:5px}
.flavor-sep{position:absolute;left:0;width:936px;height:1px;background:var(--line)}

/* confidence */
.conf-bg{left:0;top:2005px;width:1200px;height:574px;background:var(--blue-mist)}
.conf-h{left:0;top:2076px;width:1200px;font-size:30px;line-height:38px}
.card-title{position:absolute;font-family:"Archivo",sans-serif;font-weight:500;font-size:18px;line-height:26px;color:var(--blue-deep);letter-spacing:.3px}
.card-text{position:absolute;width:232px;font-size:11px;line-height:19px;color:var(--grey)}
.card-link{position:absolute;font-size:11.5px;color:var(--blue-deep);text-decoration:underline}

/* fundraise */
.fund-box{left:611px;top:2767px;width:434px;height:412px;background:var(--blue-deep);color:var(--white);text-align:center;font-size:14px;line-height:22.5px}
.fund-box p{position:absolute;left:60px;width:314px}
.fund-btn{position:absolute;left:148px;top:266px;width:138px;height:43px;border:1.5px solid var(--white);border-radius:8px;display:flex;align-items:center;justify-content:center;font-size:14px;font-weight:500}

/* reviews */
.review-text{left:214px;top:3412px;width:400px;font-size:12.5px;line-height:22.5px;color:var(--grey)}
.review-name{left:212px;top:3543px;font-size:15px;color:var(--blue-deep)}
.avatar{position:absolute;width:76px;height:76px;border-radius:50%;background:linear-gradient(160deg,#8a6e5c,#3e3a3a);border:2px solid #dfe6ee}

/* cta */
.cta-bg{left:0;top:3685px;width:1200px;height:383px;background:var(--blue-mist)}
.cta-h{left:172px;top:3762px;font-family:"Archivo",sans-serif;font-weight:500;font-size:33px;line-height:38px;letter-spacing:.5px}
.cta-p{left:172px;top:3850px;width:410px;font-size:11.5px;line-height:21px;color:var(--grey)}

/* footer */
.footer{left:0;top:4068px;width:1200px;height:318px;background:var(--blue-deep);color:var(--white)}
.foot-logo{position:absolute;left:60px;top:64px;font-size:48px;font-weight:300;color:var(--blue-soft)}
.foot-contact{position:absolute;left:60px;font-size:12px;display:flex;align-items:center;gap:14px}
.foot-col{position:absolute;top:63px;font-size:11px}
.foot-col h4{font-size:12px;font-weight:500;letter-spacing:.5px;margin-bottom:15px}
.foot-col li{list-style:none;line-height:22.6px}
.social{position:absolute;top:101px;width:33px;height:33px;border-radius:50%;border:1.5px solid var(--blue-soft)}
.copyright{position:absolute;left:0;top:283px;width:1200px;text-align:center;font-size:11px;color:var(--blue-pale)}
</style>
</head>
<body>

<!-- Header & hero -->
<div class="abs hero-bg"></div>
<div class="abs hero-ghost">VANDU</div>
<div class="abs logo">Vandu</div>
<nav class="abs nav">
  <span class="active">Home</span><span>Sell Online</span><span>About Vandu</span><span>Fundraise</span><span>Customize</span><span>Explore</span>
</nav>
<div class="abs btn-login">LOGIN</div>
<div class="btn btn-start-top">GET STARTED</div>

<h1 class="abs hero-title" style="top:140px">HEART OF THE HIGHLANDS</h1>
<h1 class="abs hero-title" style="top:242px">FOR HIGH QUALITY !</h1>

<div class="dots" style="left:165px;top:333px;width:90px;height:84px"></div>
<div class="dots" style="left:565px;top:620px;width:90px;height:32px"></div>
<div class="dots" style="left:1140px;top:170px;width:60px;height:120px"></div>

<div class="photo" role="img" aria-label="Roasted coffee grounds with a scoop" style="left:0;top:363px;width:218px;height:258px;background:linear-gradient(150deg,#8a5a33,#3c2212)"></div>
<div class="photo" role="img" aria-label="Athlete holding a coffee cup at sunset" style="left:247px;top:453px;width:218px;height:258px;background:linear-gradient(180deg,#d9a566,#4a3a2e)"></div>
<div class="photo" role="img" aria-label="Close up of falling coffee beans" style="left:490px;top:363px;width:218px;height:258px;background:linear-gradient(160deg,#7a4524,#2a140a)"></div>
<div class="photo" role="img" aria-label="Smiling woman holding a cup of coffee" style="left:735px;top:453px;width:218px;height:258px;background:linear-gradient(170deg,#b89a84,#5b463c)"></div>
<div class="photo" role="img" aria-label="Man drinking from a bottle after training" style="left:982px;top:363px;width:218px;height:258px;background:linear-gradient(160deg,#7d7aa0,#c4a48a)"></div>

<!-- Welcome -->
<div class="abs welcome-bg"></div>
<div class="abs welcome-tag">Welcome To</div>
<div class="abs welcome-bar"></div>
<div class="photo" role="img" aria-label="Sports team huddling on a grass field" style="left:141px;top:878px;width:509px;height:410px;background:linear-gradient(180deg,#9fb0b8 0%,#4c5a3e 60%,#6b6a3a 100%)"></div>
<h2 class="abs welcome-h">I SELL COFFEE TO<br>SPORTS TEAMS</h2>
<div class="abs welcome-p">
  <p>Our Arabica beans are grown at an altitude of 1600–2100' with a humidity level of 10.5–11.5%. These are prime growing conditions to produce a high level of quality and flavor levels for this type of bean.</p>
  <p>Using these conditions to grow our beans translates into several different flavor notes and types of arabica bean, that are then naturally dried and stored in eco-friendly ecotact bags to ensure maximum freshness.</p>
</div>
<div class="btn" style="left:701px;top:1173px;width:131px;height:40px">SHOP NOW</div>

<!-- Flavors -->
<h2 class="abs h-section" style="left:0;top:1363px;width:1200px">DIFFRENT COFFEE<br>FLAVORS</h2>
<div class="abs flavor-sub">Our Coffee comes in three Different Roasts:</div>

<div class="flavor-row" style="top:1498px">
  <div class="flavor-circle" style="top:0"><div class="flavor-bag">Vandu</div></div>
  <div class="flavor-name" style="top:38px">Medium Roast</div>
  <div class="flavor-desc" style="top:67px">Lorem Ipsum has been the industry's standard dummy text ever since</div>
  <div class="flavor-price" style="top:45px">$15<small>(12 oz)</small></div>
  <div class="btn" style="left:815px;top:41px;width:121px;height:41px">SHOP NOW</div>
  <div class="flavor-sep" style="top:138px"></div>
</div>
<div class="flavor-row" style="top:1651px">
  <div class="flavor-circle" style="top:0"><div class="flavor-bag">Vandu</div></div>
  <div class="flavor-name" style="top:33px">Dark Roast</div>
  <div class="flavor-desc" style="top:61px">Lorem Ipsum has been the industry's standard dummy text ever since</div>
  <div class="flavor-price" style="top:40px">$15<small>(12 oz)</small></div>
  <div class="btn" style="left:815px;top:42px;width:121px;height:41px">SHOP NOW</div>
  <div class="flavor-sep" style="top:133px"></div>
</div>
<div class="flavor-row" style="top:1799px">
  <div class="flavor-circle" style="top:0"><div class="flavor-bag">Vandu</div></div>
  <div class="flavor-name" style="top:33px">French Roast</div>
  <div class="flavor-desc" style="top:61px">Lorem Ipsum has been the industry's standard dummy text ever since</div>
  <div class="flavor-price" style="top:40px">$15<small>(12 oz)</small></div>
  <div class="btn" style="left:815px;top:38px;width:121px;height:41px">SHOP NOW</div>
  <div class="flavor-sep" style="top:133px"></div>
</div>

<!-- Confidence -->
<div class="abs conf-bg"></div>
<div class="dots" style="left:0;top:2025px;width:55px;height:110px"></div>
<div class="dots" style="left:911px;top:2545px;width:88px;height:84px"></div>
<h2 class="abs h-section conf-h">WE HAVE THE CONFIDENCE IN OUR SKILLSET<br>FROM OUR LONG HISTORY OF PRODUCTION<br>TO GRANT YOU PREMIUM COFFEE</h2>

<div class="photo" role="img" aria-label="Cup of coffee with heart shaped steam" style="left:72px;top:2245px;width:188px;height:236px;transform:rotate(-9deg);background:linear-gradient(160deg,#4a3124,#a07a5a)"></div>
<div class="card-title" style="left:294px;top:2258px">COFFEE WITH A<br>PURPOSE</div>
<div class="card-text" style="left:294px;top:2320px">Highland Heart Coffee Co. operates as a large-scale coffee growing and harvesting company located within the community of Valle Alto.</div>
<div class="card-link" style="left:296px;top:2413px">Learn More</div>

<div class="photo" role="img" aria-label="Espresso machine portafilter with ground coffee" style="left:575px;top:2245px;width:188px;height:236px;transform:rotate(-9deg);background:linear-gradient(160deg,#2a2a2c,#c9772e)"></div>
<div class="card-title" style="left:803px;top:2258px">THE MOST AMAZING<br>COFFEE STATISTICS</div>
<div class="card-text" style="left:803px;top:2320px">64% of American adults currently consume coffee every day. Americans drink about 400 million cups of coffee every day...</div>
<div class="card-link" style="left:805px;top:2413px">Learn More</div>

<div class="photo" role="img" aria-label="Hands reaching together" style="left:1110px;top:2237px;width:130px;height:236px;transform:rotate(9deg);background:linear-gradient(160deg,#d8c6b8,#8a5a3c)"></div>

<!-- Fundraising -->
<h2 class="abs h-section" style="left:0;top:2653px;width:1200px">FUNDRAISING FOR CLUBS, SPORTS<br>TEAMS AND/OR &nbsp;ORGANIZATIONS</h2>
<div class="photo" role="img" aria-label="Group of students sitting on outdoor steps with a laptop" style="left:153px;top:2767px;width:436px;height:412px;background:linear-gradient(180deg,#c9b79a 0%,#8c8a84 45%,#b4b2ae 100%)"></div>
<div class="abs fund-box">
  <p style="top:74px">This coffee will be a great product for students to fundraise with, and support their respective clubs, sports teams and/or organizations.</p>
  <p style="top:175px">Coffee is &nbsp;such a widely enjoyed commodity that students will have great success in raising money for their chosen cause.</p>
  <div class="fund-btn">LEARN MORE</div>
</div>

<!-- Reviews -->
<h2 class="abs h-section" style="left:0;top:3252px;width:1200px">CLIENT REVIEWS</h2>
<svg class="abs" style="left:220px;top:3362px" width="34" height="24" viewBox="0 0 34 24" aria-hidden="true">
  <polygon points="8,0 16,0 9,24 0,24" fill="var(--blue-deep)"/>
  <polygon points="26,0 34,0 27,24 18,24" fill="var(--blue-deep)"/>
</svg>
<p class="abs review-text">" Lorem Ipsum has been the industry's standard dummy text ever since the when an unknown printer took a galley of type and scrambled it to make a type specimen book. It has survived not only five centuries, but also the leap into electronic typesetting, remaining essentially unchanged. "</p>
<div class="abs review-name">–&nbsp;&nbsp; Client Name</div>
<svg class="abs" style="left:213px;top:3582px" width="76" height="16" aria-hidden="true">
  <circle cx="8" cy="8" r="6" fill="none" stroke="var(--blue-mid)" stroke-width="1.5"/>
  <circle cx="27" cy="8" r="6" fill="var(--blue-pale)"/>
  <circle cx="46" cy="8" r="6" fill="none" stroke="var(--blue-mid)" stroke-width="1.5"/>
  <circle cx="65" cy="8" r="6" fill="none" stroke="var(--blue-mid)" stroke-width="1.5"/>
</svg>
<div class="abs" style="left:737px;top:3361px;width:1px;height:230px;background:var(--line)"></div>
<div class="avatar" role="img" aria-label="Client portrait" style="left:896px;top:3337px"></div>
<div class="avatar" role="img" aria-label="Client portrait" style="left:805px;top:3381px"></div>
<div class="avatar" role="img" aria-label="Client portrait" style="left:896px;top:3434px"></div>
<div class="avatar" role="img" aria-label="Client portrait" style="left:805px;top:3487px"></div>
<div class="avatar" role="img" aria-label="Client portrait" style="left:896px;top:3531px"></div>

<!-- Call to action -->
<div class="abs cta-bg"></div>
<div class="dots" style="left:46px;top:3651px;width:88px;height:84px"></div>
<div class="dots" style="left:1128px;top:3915px;width:72px;height:110px"></div>
<h2 class="abs cta-h">WE ARE WITH YOU EVERY<br>STEP OF THE WAY</h2>
<p class="abs cta-p">If you any questions or concerns, please feel free to reach out to me, Tomas Vega. My contact information is listed in the beginning of this brochure. We know the recipients of our fine coffee will enjoy it as much as we do</p>
<div class="btn" style="left:172px;top:3947px;width:138px;height:41px">GET STARTED</div>
<div class="abs" style="left:705px;top:3749px;width:337px;height:4px;background:var(--blue-deep)"></div>
<div class="photo" role="img" aria-label="Smiling woman holding a coffee cup by a window" style="left:705px;top:3753px;width:337px;height:332px;background:linear-gradient(160deg,#dcd6cc 0%,#9a7a62 55%,#6f7f6a 100%)"></div>

<!-- Footer -->
<footer class="abs footer">
  <div class="foot-logo">Vandu</div>
  <div class="foot-contact" style="top:135px">
    <svg width="16" height="16" viewBox="0 0 24 24" aria-hidden="true"><path d="M6.6 10.8a15 15 0 0 0 6.6 6.6l2.2-2.2c.3-.3.7-.4 1-.2 1.1.4 2.3.6 3.6.6.6 0 1 .4 1 1V20c0 .6-.4 1-1 1A17 17 0 0 1 3 4c0-.6.4-1 1-1h3.5c.6 0 1 .4 1 1 0 1.3.2 2.5.6 3.6.1.3 0 .7-.2 1z" fill="var(--blue-pale)"/></svg>
    <span>555-014-2290</span>
  </div>
  <div class="foot-contact" style="top:161px">
    <svg width="16" height="13" viewBox="0 0 24 18" aria-hidden="true"><rect width="24" height="18" rx="2" fill="var(--blue-pale)"/><path d="M1 2l11 8 11-8" fill="none" stroke="var(--blue-deep)" stroke-width="2"/></svg>
    <span>tomasvega@vandumail.com</span>
  </div>
  <div class="foot-col" style="left:281px"><h4>SITEMAP</h4><ul><li>Sell Online</li><li>About Vandu</li><li>Fundraise</li><li>Customize</li><li>Explore</li></ul></div>
  <div class="foot-col" style="left:500px"><h4>RESOURCES</h4><ul><li>Help Center</li><li>Blog</li><li>Fundraise</li><li>Login</li></ul></div>
  <div class="foot-col" style="left:720px"><h4>COMPANY</h4><ul><li>About</li><li>Careers</li><li>Reviews</li><li>Contact</li><li>Privacy</li><li>Terms</li></ul></div>
  <div class="foot-col" style="left:940px"><h4>FOLLOW US</h4></div>
  <div class="social" style="left:937px" aria-label="Social profile"></div>
  <div class="social" style="left:976px" aria-label="Social profile"></div>
  <div class="social" style="left:1015px" aria-label="Social profile"></div>
  <div class="copyright">©Vandu - 2021 All rights reserved.</div>
</footer>

</body>
</html>
```